business card for LWR pty ltd

We require a business card that stands out . I have included our company flyer and would like the services listed to be put on the card so when we Give out the cards to customers they have an idea of services we provide. need the winning design to be in editable photo shop format, editable iMac pages format or editable windows publisher format, so that I can enter in names, email addresses, phone numbers etc myself. I have included a pdf documents of info / items needed on the card to use as reference please.
Updates

need more submissions

Need extra days to review

Sick

Target Market(s)

new customers

Contact Information for Business Card

details are on attached business card requirements file

Requirements
Must have
• I have attached a list of must haves

```html
<!DOCTYPE html>
<html lang="en">
<head>
<meta charset="utf-8">
<title>LWR pty ltd – Business Card</title>
<link href="https://fonts.googleapis.com/css2?family=Arimo:wght@400;700&family=Archivo+Black&display=swap" rel="stylesheet">
<style>
  :root {
    --page-bg: #2a2a2c;
    --card-bg: #1a181c;
    --card-edge: #0f0e11;
    --text-light: #f2f2f2;
    --text-muted: #d9d9d9;
    --accent-gold: #c9a46a;
    --mesh-dark: #141416;
    --mesh-mid: #3a3a3e;
    --mesh-light: #6c6c72;
  }
  * { margin: 0; padding: 0; box-sizing: border-box; }
  html, body {
    width: 1200px;
    height: 900px;
    overflow: hidden;
    background: var(--page-bg);
    font-family: "Arimo", Arial, sans-serif;
  }
  .sheet {
    width: 1200px;
    height: 900px;
    display: flex;
    flex-direction: column;
    align-items: center;
    justify-content: center;
    gap: 36px;
  }
  .card {
    position: relative;
    width: 700px;
    height: 400px;
    background: var(--card-bg);
    overflow: hidden;
    box-shadow: 0 10px 28px rgba(0,0,0,0.55);
  }

  /* Back: services */
  .services {
    position: absolute;
    top: 52px;
    left: 0;
    width: 100%;
    text-align: center;
    color: var(--text-light);
    font-size: 19px;
    line-height: 1.42;
  }
  .services .dot { margin: 0 4px; }
  .fleet-photo {
    position: absolute;
    left: 150px;
    right: 0;
    bottom: 0;
    height: 175px;
    background:
      linear-gradient(180deg, rgba(26,24,28,1) 0%, rgba(26,24,28,0) 30%),
      linear-gradient(90deg, #4a4540 0%, #2e2b2a 35%, #3a3633 65%, #2a2828 100%);
  }

  /* Front: identity */
  .mesh-band {
    position: absolute;
    top: 0;
    left: 0;
    width: 100%;
    height: 225px;
    background:
      radial-gradient(ellipse at 55% 45%, var(--mesh-light) 0%, var(--mesh-mid) 35%, var(--mesh-dark) 80%);
  }
  .brand-name {
    position: absolute;
    top: 0;
    left: 0;
    width: 100%;
    height: 225px;
    display: flex;
    align-items: center;
    justify-content: center;
    font-family: "Arimo", Arial, sans-serif;
    font-weight: 700;
    font-size: 60px;
    color: var(--text-light);
    letter-spacing: 1px;
  }
  .person {
    position: absolute;
    left: 40px;
    bottom: 34px;
    color: var(--text-light);
  }
  .person-name {
    font-family: "Archivo Black", "Arial Black", sans-serif;
    font-size: 30px;
    color: var(--accent-gold);
    text-transform: uppercase;
    letter-spacing: 0.5px;
    line-height: 1.1;
  }
  .person-role {
    font-size: 20px;
    margin-top: 4px;
  }
  .person-address {
    font-size: 20px;
    line-height: 1.3;
    margin-top: 22px;
  }
  .contacts {
    position: absolute;
    right: 30px;
    top: 244px;
    list-style: none;
    text-align: right;
    color: var(--text-light);
    font-size: 19px;
    line-height: 1.35;
  }
  .contacts li {
    display: flex;
    align-items: center;
    justify-content: flex-end;
    gap: 8px;
  }
  .contacts svg { width: 18px; height: 18px; flex: none; }
</style>
</head>
<body>
<main class="sheet">

  <section class="card card-back">
    <p class="services">
      Over size loads/Hot shot Loads<span class="dot">●</span>Heavy Vehicle Recovery services<br>
      Potable water Deliveries<span class="dot">●</span>Road Building/Maintenance<br>
      Earthworks<span class="dot">●</span>Sand &amp; Metal Supply &amp; Cartage<br>
      Road Train Tippers<span class="dot">●</span>Road Train Tankers<br>
      Road Train Flat Tops<span class="dot">●</span>Drop Deck Trailers<br>
      Mine site accredited equipment &amp; Operators
    </p>
    <div class="fleet-photo" role="img" aria-label="Photo of a road train truck with three tipper trailers on a dark perforated metal texture"></div>
  </section>

  <section class="card card-front">
    <div class="mesh-band" role="img" aria-label="Dark perforated metal mesh texture"></div>
    <div class="brand-name">LWR pty ltd</div>

    <div class="person">
      <h1 class="person-name">Daniel Reeve</h1>
      <p class="person-role">Director</p>
      <p class="person-address">Lot 444 example<br>address Australia</p>
    </div>

    <ul class="contacts">
      <li>000 444 000
        <svg viewBox="0 0 24 24" aria-hidden="true"><path fill="var(--accent-gold)" d="M6.6 10.8a15.1 15.1 0 0 0 6.6 6.6l2.2-2.2a1 1 0 0 1 1-.25 11.4 11.4 0 0 0 3.6.57 1 1 0 0 1 1 1V20a1 1 0 0 1-1 1A17 17 0 0 1 3 4a1 1 0 0 1 1-1h3.5a1 1 0 0 1 1 1c0 1.25.2 2.45.57 3.57a1 1 0 0 1-.25 1z"/></svg>
      </li>
      <li>email@lwrservices.com.au
        <svg viewBox="0 0 24 24" aria-hidden="true"><rect x="2" y="5" width="20" height="14" fill="var(--accent-gold)"/><path d="M2 5l10 8 10-8" fill="none" stroke="var(--card-bg)" stroke-width="1.6"/></svg>
      </li>
      <li>www.lwrservices.com.au
        <svg viewBox="0 0 24 24" aria-hidden="true"><g fill="none" stroke="var(--accent-gold)" stroke-width="1.8"><circle cx="12" cy="12" r="9.5"/><ellipse cx="12" cy="12" rx="4.2" ry="9.5"/><path d="M2.5 12h19M4 7h16M4 17h16"/></g></svg>
      </li>
    </ul>
  </section>

</main>
</body>
</html>
```